みなせ權兵衛太鼓をモチーフに、この藤田の地を干拓した様に力強くシンプルなパッケージができたらと思います。
色は2~3色程度。文字のキーワードとして①岡山②みなせ權兵衛③どら焼きの文字を入れたいと思います。※漢字・ひらがな・ローマ字等のフォントはお任せ致します。
http://www.kasumi-sangyo.example/
※最悪、岡山はなくてもOKです。
寸法は写真添付しております。
グレー系
• 高解像度JPG (.jpg)
• イラストレーター形式 (.ai)
どら焼きの文字が有っても無くても、短縮(〜どら、〜ドラ)でもOKです。
大太鼓のイメージです。影絵的にしても面白いかもしれません。参考までに。

一番イメージに近いデザインでした!

皆様、たくさんの素敵なデザインのご提案を頂きありがとうございました。それぞれが個性ある素敵な作品ばかりで、決定するのに時間かかりました。心から感謝いたします。
また機会ございましたら何卒よろしくお願い申し上げます。

```html
<!DOCTYPE html>
<html lang="ja">
<head>
<meta charset="utf-8">
<title>みなせ權兵衛 どら焼 パッケージ</title>
<link rel="stylesheet" href="https://fonts.googleapis.com/css2?family=Yuji+Syuku&family=Shippori+Mincho:wght@500&display=swap">
<style>
  :root {
    --page: #ffffff;
    --wrapper: #e4e4e4;
    --wrapper-edge: #d6d6d6;
    --disc: #ffffff;
    --halo-inner: #c9b8a4;
    --halo-outer: #e4e4e4;
    --ink: #2a2a2a;
    --crimson: #8c2233;
  }
  * { margin: 0; padding: 0; box-sizing: border-box; }
  html, body { width: 848px; height: 1200px; overflow: hidden; background: var(--page); }
  .canvas { position: relative; width: 848px; height: 1200px; }

  .package { position: absolute; left: 113px; width: 628px; height: 440px; }
  .package--halo { top: 113px; }
  .package--plain { top: 637px; }

  .wrapper-shape { position: absolute; inset: 0; width: 100%; height: 100%; }

  .halo {
    position: absolute; left: 106px; top: 12px; width: 412px; height: 412px; border-radius: 50%;
    background: radial-gradient(circle, var(--halo-inner) 0%, var(--halo-inner) 62%, var(--halo-outer) 72%);
  }
  .drum-crest {
    position: absolute; left: 162px; top: 68px; width: 300px; height: 300px; border-radius: 50%;
    background: var(--disc);
  }

  .maker-name {
    position: absolute; left: 372px; top: 70px;
    font-family: "Shippori Mincho", serif; font-weight: 500; font-size: 26px; line-height: 1;
    color: var(--ink); letter-spacing: 1px; white-space: nowrap;
  }
  .product-name {
    position: absolute; left: 254px; top: 96px; width: 100px;
    font-family: "Yuji Syuku", serif; font-weight: 400; font-size: 96px; line-height: 1;
    color: var(--ink); text-align: center;
  }
  .product-name span { display: block; height: 96px; }
  .place-name {
    position: absolute; left: 150px; top: 262px;
    font-family: "Shippori Mincho", serif; font-weight: 500; font-size: 22px; line-height: 1;
    color: var(--ink); letter-spacing: 2px; white-space: nowrap;
  }

  .figure {
    position: absolute; background: var(--crimson); opacity: 0.9; border-radius: 30% 40% 20% 30%;
  }
  .figure--left { left: 120px; top: 300px; width: 82px; height: 72px; }
  .figure--right { left: 430px; top: 296px; width: 80px; height: 76px; }
  .drum-icon {
    position: absolute; left: 372px; top: 312px; width: 48px; height: 56px;
    background: var(--crimson); border-radius: 6px;
  }
</style>
</head>
<body>
<main class="canvas">

  <section class="package package--halo" aria-label="どら焼 包装 (茶の光輪あり)">
    <svg class="wrapper-shape" viewBox="0 0 628 440" preserveAspectRatio="none" aria-hidden="true">
      <path fill="var(--wrapper)" stroke="var(--wrapper-edge)" stroke-width="1"
        d="M10 0 H618 L628 11 L618 22 L628 33 L618 44 L628 55 L618 66 L628 77 L618 88 L628 99 L618 110 L628 121 L618 132 L628 143 L618 154 L628 165 L618 176 L628 187 L618 198 L628 209 L618 220 L628 231 L618 242 L628 253 L618 264 L628 275 L618 286 L628 297 L618 308 L628 319 L618 330 L628 341 L618 352 L628 363 L618 374 L628 385 L618 396 L628 407 L618 418 L628 429 L618 440 H10 L0 429 L10 418 L0 407 L10 396 L0 385 L10 374 L0 363 L10 352 L0 341 L10 330 L0 319 L10 308 L0 297 L10 286 L0 275 L10 264 L0 253 L10 242 L0 231 L10 220 L0 209 L10 198 L0 187 L10 176 L0 165 L10 154 L0 143 L10 132 L0 121 L10 110 L0 99 L10 88 L0 77 L10 66 L0 55 L10 44 L0 33 L10 22 L0 11 Z"/>
    </svg>
    <div class="halo" aria-hidden="true"></div>
    <div class="drum-crest" role="img" aria-label="太鼓の巴紋を思わせる白い円形の装飾"></div>
    <p class="maker-name">みなせ權兵衛</p>
    <h1 class="product-name"><span>ど</span><span>ら</span><span>焼</span></h1>
    <p class="place-name">おかやま</p>
    <div class="figure figure--left" role="img" aria-label="撥を構える人物の影絵"></div>
    <div class="drum-icon" role="img" aria-label="大太鼓の影絵"></div>
    <div class="figure figure--right" role="img" aria-label="太鼓を打つ人物の影絵"></div>
  </section>

  <section class="package package--plain" aria-label="どら焼 包装 (無地)">
    <svg class="wrapper-shape" viewBox="0 0 628 440" preserveAspectRatio="none" aria-hidden="true">
      <path fill="var(--wrapper)" stroke="var(--wrapper-edge)" stroke-width="1"
        d="M10 0 H618 L628 11 L618 22 L628 33 L618 44 L628 55 L618 66 L628 77 L618 88 L628 99 L618 110 L628 121 L618 132 L628 143 L618 154 L628 165 L618 176 L628 187 L618 198 L628 209 L618 220 L628 231 L618 242 L628 253 L618 264 L628 275 L618 286 L628 297 L618 308 L628 319 L618 330 L628 341 L618 352 L628 363 L618 374 L628 385 L618 396 L628 407 L618 418 L628 429 L618 440 H10 L0 429 L10 418 L0 407 L10 396 L0 385 L10 374 L0 363 L10 352 L0 341 L10 330 L0 319 L10 308 L0 297 L10 286 L0 275 L10 264 L0 253 L10 242 L0 231 L10 220 L0 209 L10 198 L0 187 L10 176 L0 165 L10 154 L0 143 L10 132 L0 121 L10 110 L0 99 L10 88 L0 77 L10 66 L0 55 L10 44 L0 33 L10 22 L0 11 Z"/>
    </svg>
    <div class="drum-crest" role="img" aria-label="太鼓の巴紋を思わせる白い円形の装飾"></div>
    <p class="maker-name">みなせ權兵衛</p>
    <h2 class="product-name"><span>ど</span><span>ら</span><span>焼</span></h2>
    <p class="place-name">おかやま</p>
    <div class="figure figure--left" role="img" aria-label="撥を構える人物の影絵"></div>
    <div class="drum-icon" role="img" aria-label="大太鼓の影絵"></div>
    <div class="figure figure--right" role="img" aria-label="太鼓を打つ人物の影絵"></div>
  </section>

</main>
</body>
</html>
```